Manufacturing Company Business card

K & T is a leading supplier of complex machine parts, assemblies and sub assemblies to the aerospace industry.
we would like to create a new feel for our manufacturing company business card design.
We are into lean manufacturing, bold design, metal, use current logo, use "this is your life" logo for entire back of card. updated look for 2015, text, bardcode, etc

our primary end use is flight control components used on about all commercial and business jets in use as well as military aircraft and civil aviation.
Updates

Reason: Need more time to review with internal team at KTmfg:)

Target Market(s)

aerospace, manufacturing

Industry/Entity Type

Aero

Contact Information for Business Card

New, industrial, trendy, use current logo, we like text, vmail is lame :( cell ph is ok - what is a fax???

Font styles to use
Serif
Sans Serif

Requirements
Must have
• incorporate our current logo, one option is an Industrial look, metal etc. we can also try to incorporate the feel of the back of the card onto the front but not so busy.
• Back of card full size "this is your life"
• front side, barcode, cell, - our motto "solutions in manufacturing" tm
Nice to have
• Professional look
• up to date
• appeals to broad audience
Should not have
• too much content - pictures of planes

```html
<!DOCTYPE html>
<html lang="en">
<head>
<meta charset="utf-8">
<title>K &amp; T Manufacturing Business Card</title>
<link rel="stylesheet" href="https://fonts.googleapis.com/css2?family=Open+Sans:wght@400;600;700&display=swap">
<style>
  :root {
    --brand-green: #03a05a;
    --card-white: #ececea;
    --ink-dark: #1c1c1a;
    --ring-grey: #b9b9b6;
    --backdrop: #8e8e8c;
    --text-light: #ffffff;
  }
  * { margin: 0; padding: 0; box-sizing: border-box; }
  html, body {
    width: 1200px; height: 900px; overflow: hidden;
    background: var(--backdrop);
    font-family: "Open Sans", Arial, sans-serif;
  }
  .canvas { position: relative; width: 1200px; height: 900px; }

  .card {
    position: absolute; left: 290px; width: 620px; height: 354px;
    background: var(--card-white); overflow: hidden;
    box-shadow: 0 6px 18px rgba(0,0,0,0.25);
  }
  .card-back { top: 68px; }
  .card-front { top: 476px; }

  /* Back side */
  .back-band-top { position: absolute; left: 0; top: 0; width: 100%; height: 66px; background: var(--brand-green); }
  .back-band-bottom { position: absolute; left: 0; top: 300px; width: 100%; height: 22px; background: var(--brand-green); }

  .wordmark {
    position: absolute; display: flex; align-items: center; gap: 14px;
    color: var(--ink-dark); font-weight: 700; letter-spacing: 0.04em;
  }
  .wordmark-dot {
    flex: none; border: 2px solid var(--ring-grey); border-radius: 50%;
  }
  .card-back .wordmark { left: 150px; top: 150px; font-size: 27px; }
  .card-back .wordmark-dot { width: 44px; height: 44px; }

  /* Front side */
  .front-band { position: absolute; left: 0; top: 168px; width: 100%; height: 152px; background: var(--brand-green); }
  .card-front .wordmark { left: 250px; top: 70px; font-size: 22px; }
  .card-front .wordmark-dot { width: 36px; height: 36px; }

  .person { position: absolute; left: 30px; top: 176px; color: var(--text-light); }
  .person-name { font-size: 24px; font-weight: 700; line-height: 1.1; }
  .person-title { font-size: 14px; font-weight: 400; margin-top: 2px; }

  .contact-list {
    position: absolute; right: 26px; top: 214px; list-style: none;
    color: var(--text-light); font-size: 16px; line-height: 20px; text-align: right;
  }
  .contact-list li { display: flex; justify-content: flex-end; align-items: center; gap: 10px; }
  .contact-icon { width: 12px; height: 12px; flex: none; fill: var(--text-light); }
</style>
</head>
<body>
<main class="canvas">

  <section class="card card-back" aria-label="Card back">
    <div class="back-band-top"></div>
    <div class="wordmark"><span class="wordmark-dot"></span><span>K &amp; T MANUFACTURING</span></div>
    <div class="back-band-bottom"></div>
  </section>

  <section class="card card-front" aria-label="Card front">
    <div class="wordmark"><span class="wordmark-dot"></span><span>K &amp; T MANUFACTURING</span></div>
    <div class="front-band"></div>
    <div class="person">
      <p class="person-name">Daniel Reyes</p>
      <p class="person-title">Managing Director</p>
    </div>
    <ul class="contact-list">
      <li>123.456.7890
        <svg class="contact-icon" viewBox="0 0 12 12"><path d="M1 4c0-2 2-3 5-3s5 1 5 3v1H8V3.5H4V5H1z M2.5 6h7l1 5h-9z"/></svg></li>
      <li>123.456.7890
        <svg class="contact-icon" viewBox="0 0 12 12"><path d="M3 0h6v12H3z M4 1.5v7h4v-7z"/></svg></li>
      <li>info@youremail.com
        <svg class="contact-icon" viewBox="0 0 12 12"><path d="M0 2h12v8H0z M1 3l5 3.5L11 3v-.2H1z" fill-rule="evenodd"/></svg></li>
      <li>www.website.com
        <svg class="contact-icon" viewBox="0 0 12 12"><path d="M5 7l2-2M4.5 5.5l-2 2a1.6 1.6 0 0 0 2 2l2-2M7.5 6.5l2-2a1.6 1.6 0 0 0-2-2l-2 2" stroke="#fff" stroke-width="1.4" fill="none" stroke-linecap="round"/></svg></li>
      <li>1234, Address Goes Here, Country Name, 123456
        <svg class="contact-icon" viewBox="0 0 12 12"><path d="M6 0a4 4 0 0 1 4 4c0 3-4 8-4 8S2 7 2 4a4 4 0 0 1 4-4zm0 2.5a1.5 1.5 0 1 0 0 3 1.5 1.5 0 0 0 0-3z" fill-rule="evenodd"/></svg></li>
    </ul>
  </section>

</main>
</body>
</html>
```